Flyer for Consulting Services (PM+Dev-Lead)

• The attached document describes consulting services for StartUps or young companies with a digital buisness model. We provide services for product management and development lead/scrum master. The target group of the flyer (i.e. who reads that flyer) is CEOs of Startups, Founders, Investors, Business Angle.s
• The task is to design an A4 flyer with one page layout (one pager) mostly for electronic destribution (printing second choice). There have to be two versions according given input: one in German and one in English with same layout. Preferably a format which allows us to adjust wording (e.g. Word, MS Publisher, …)
The final design should deliver professionality on one side and agility/StartUp mentality on the other side.

```html
<!DOCTYPE html>
<html lang="en">
<head>
<meta charset="utf-8">
<title>Product Management &amp; Development Partner – Flyer</title>
<link rel="stylesheet" href="https://fonts.googleapis.com/css2?family=Bebas+Neue&family=Open+Sans:wght@400;600;700&display=swap">
<style>
  :root {
    --blue: #1a93d0;
    --blue-deep: #0f74ad;
    --dark: #2b2b2b;
    --light: #f3f3f3;
    --ink: #1f1f1f;
    --muted: #555555;
    --on-dark: #e6e6e6;
    --white: #ffffff;
  }
  * { margin: 0; padding: 0; box-sizing: border-box; }
  html, body { width: 849px; height: 1200px; overflow: hidden; background: var(--white); }
  .flyer {
    position: relative; width: 849px; height: 1200px; overflow: hidden;
    font-family: "Open Sans", Arial, sans-serif; color: var(--ink);
  }

  /* hero */
  .hero-photo {
    position: absolute; left: 0; top: 0; width: 849px; height: 437px;
    background: linear-gradient(180deg, #6f7478 0%, #5a5f63 45%, #4a4e52 70%, #3a3c3f 100%);
  }
  .headline {
    position: absolute; left: 0; top: 28px; width: 849px; text-align: center;
    font-family: "Bebas Neue", Impact, sans-serif; font-weight: 400;
    font-size: 42px; line-height: 44px; letter-spacing: 2.4px; color: var(--white);
  }

  /* left column */
  .audience {
    position: absolute; left: 0; top: 437px; width: 426px; height: 763px; background: var(--light);
  }
  .audience-title {
    position: absolute; left: 28px; top: 28px;
    font-family: "Bebas Neue", Impact, sans-serif; font-size: 74px; line-height: 74px; color: var(--ink);
  }
  .question {
    position: absolute; left: 36px; display: flex; align-items: center; width: 390px;
  }
  .question svg { flex: none; width: 76px; height: 86px; }
  .question p {
    margin-left: 14px; font-size: 22.5px; line-height: 26px; color: var(--ink);
  }
  .q1 { top: 110px; } .q2 { top: 218px; } .q3 { top: 325px; }
  .divider { position: absolute; left: 32px; top: 462px; width: 375px; height: 1px; background: #c9c9c9; }
  .contact-title {
    position: absolute; left: 37px; top: 474px; font-weight: 700; font-size: 19.5px; letter-spacing: .3px;
  }
  .person { position: absolute; left: 37px; font-size: 14.5px; line-height: 22px; color: #333; }
  .person .line { display: flex; align-items: center; color: var(--muted); }
  .person svg { width: 12px; height: 12px; margin-right: 8px; }
  .p1 { top: 518px; } .p2 { top: 630px; }

  /* right column */
  .offer {
    position: absolute; left: 426px; top: 437px; width: 423px; height: 763px; background: var(--dark);
  }
  .bar {
    position: absolute; left: -2px; width: 425px; height: 54px; background: var(--blue);
    color: var(--white); font-size: 23px; line-height: 54px; padding-left: 9px;
  }
  .bar::after {
    content: ""; position: absolute; left: 24px; bottom: -11px;
    border-left: 14px solid transparent; border-right: 14px solid transparent; border-top: 11px solid var(--blue);
  }
  .list { position: absolute; left: 19px; width: 390px; list-style: none; }
  .list li {
    position: relative; padding-left: 22px; margin-bottom: 9px;
    font-size: 14px; line-height: 15.5px; color: var(--on-dark);
  }
  .list li svg { position: absolute; left: 0; top: 1px; width: 15px; height: 15px; }
  .b1 { top: 0; }   .l1 { top: 78px; }
  .b2 { top: 243px; } .l2 { top: 320px; }
  .b3 { top: 414px; } .l3 { top: 491px; }
  .b4 { top: 603px; } .l4 { top: 682px; }
</style>
</head>
<body>
<div class="flyer">
  <svg width="0" height="0" style="position:absolute">
    <defs>
      <symbol id="tick" viewBox="0 0 16 16">
        <rect x="1" y="3" width="11" height="11" fill="none" stroke="#1a93d0" stroke-width="1.6"/>
        <path d="M4 8.5 L7 11.5 L15 2.5" fill="none" stroke="#1a93d0" stroke-width="2.2" stroke-linecap="round" stroke-linejoin="round"/>
      </symbol>
    </defs>
  </svg>

  <div class="hero-photo" role="img" aria-label="Photo of six young people sitting in a row against a grey brick wall, smiling and using tablets, phones and a laptop"></div>
  <h1 class="headline">We are your partner for product management<br>and development!</h1>

  <section class="audience">
    <div class="audience-title">You …</div>

    <div class="question q1">
      <svg viewBox="0 0 76 86" aria-hidden="true">
        <ellipse cx="38" cy="80" rx="30" ry="4" fill="#d6d6d6"/>
        <circle cx="38" cy="38" r="37" fill="#fff"/>
        <circle cx="38" cy="38" r="33" fill="var(--blue)"/>
        <circle cx="38" cy="33" r="12" fill="#fff"/>
        <rect x="32" y="43" width="12" height="9" rx="1.5" fill="#fff"/>
        <rect x="33" y="53" width="10" height="3" rx="1.5" fill="#fff"/>
        <path d="M38 45 V36 M34 35 L38 38 L42 35" stroke="var(--blue)" stroke-width="1.6" fill="none"/>
      </svg>
      <p>have a digital<br>business idea?</p>
    </div>

    <div class="question q2">
      <svg viewBox="0 0 76 86" aria-hidden="true">
        <ellipse cx="38" cy="80" rx="30" ry="4" fill="#d6d6d6"/>
        <circle cx="38" cy="38" r="37" fill="#fff"/>
        <circle cx="38" cy="38" r="33" fill="var(--blue)"/>
        <rect x="22" y="27" width="32" height="22" rx="3" fill="#fff"/>
        <rect x="22" y="32" width="32" height="4" fill="var(--blue)"/>
        <rect x="26" y="41" width="10" height="2.5" fill="var(--blue)"/>
      </svg>
      <p>already obtained<br>a funding?</p>
    </div>

    <div class="question q3">
      <svg viewBox="0 0 76 86" aria-hidden="true">
        <ellipse cx="38" cy="80" rx="30" ry="4" fill="#d6d6d6"/>
        <circle cx="38" cy="38" r="37" fill="#fff"/>
        <circle cx="38" cy="38" r="33" fill="var(--blue)"/>
        <circle cx="25" cy="32" r="5" fill="#fff"/>
        <circle cx="51" cy="32" r="5" fill="#fff"/>
        <path d="M16 50 a9 9 0 0 1 18 0 Z M42 50 a9 9 0 0 1 18 0 Z" fill="#fff"/>
        <circle cx="38" cy="34" r="6.5" fill="#fff" stroke="var(--blue)" stroke-width="1.5"/>
        <path d="M26 55 a12 12 0 0 1 24 0 Z" fill="#fff" stroke="var(--blue)" stroke-width="1.5"/>
      </svg>
      <p>are looking for experienced<br>support for product<br>development?</p>
    </div>

    <div class="divider"></div>
    <h2 class="contact-title">HOW TO CONTACT US?</h2>

    <div class="person p1">
      <div>Lena Hartwig</div>
      <div>Agile Product Manager</div>
      <div class="line"><svg viewBox="0 0 12 12"><path d="M2 1 L4.5 1 L5.5 3.5 L4 4.8 Q5.5 7.5 7.2 8 L8.5 6.5 L11 7.5 L11 10 Q6 11 2.5 6.5 Q1 4 2 1Z" fill="var(--blue)"/></svg>+49-170-55 01 23 45</div>
      <div class="line"><svg viewBox="0 0 12 12"><rect x="0.5" y="2" width="11" height="8" fill="var(--blue)"/><path d="M0.5 2 L6 6.5 L11.5 2" stroke="#fff" stroke-width="1" fill="none"/></svg>contact@lena-hartwig.de</div>
    </div>
    <div class="person p2">
      <div>Tobias Reuter</div>
      <div>Scrum Master, Dev-Lead</div>
      <div class="line"><svg viewBox="0 0 12 12"><path d="M2 1 L4.5 1 L5.5 3.5 L4 4.8 Q5.5 7.5 7.2 8 L8.5 6.5 L11 7.5 L11 10 Q6 11 2.5 6.5 Q1 4 2 1Z" fill="var(--blue)"/></svg>+49-171-4 12 34 56</div>
      <div class="line"><svg viewBox="0 0 12 12"><rect x="0.5" y="2" width="11" height="8" fill="var(--blue)"/><path d="M0.5 2 L6 6.5 L11.5 2" stroke="#fff" stroke-width="1" fill="none"/></svg>tobias.reuter@nordvia.com</div>
    </div>
  </section>

  <section class="offer">
    <h3 class="bar b1">We …</h3>
    <ul class="list l1">
      <li><svg><use href="#tick"/></svg>take over interim roles as: Product Owner, Scrum Master, and Dev-Lead</li>
      <li><svg><use href="#tick"/></svg>create your development team, optionally with offshore/nearshore locations</li>
      <li><svg><use href="#tick"/></svg>setup the cloud environment for your solution and support its operations</li>
      <li><svg><use href="#tick"/></svg>jointly establish an agile/lean mindset including corresponding procedures</li>
    </ul>

    <h3 class="bar b2">If wanted, …</h3>
    <ul class="list l2">
      <li><svg><use href="#tick"/></svg>together we evolve your strategic orientation</li>
      <li><svg><use href="#tick"/></svg>support you in architecture and technology design</li>
      <li><svg><use href="#tick"/></svg>train you in product management and in creating a scalable agile organisation</li>
    </ul>

    <h3 class="bar b3">Your benefits …</h3>
    <ul class="list l3">
      <li><svg><use href="#tick"/></svg>you focus on your ideas and your business model</li>
      <li><svg><use href="#tick"/></svg>you receive a professional realization of your ideas – in quality, time and budget</li>
      <li><svg><use href="#tick"/></svg>our lean/agile mindset supports your start-up mentality and your commercial success</li>
    </ul>

    <h3 class="bar b4">Why us?</h3>
    <ul class="list l4">
      <li><svg><use href="#tick"/></svg>combined expertise in product management, development, and operations</li>
      <li><svg><use href="#tick"/></svg>founders with experience in digital business models and numerous industries</li>
    </ul>
  </section>
</div>
</body>
</html>
```